Letter design, envelope design, and more

Hello, we the Vortel Gmbh are looking for our shop. Letter C5. Design does not have to be like a business card, so it can have straight lines. Only the color is important. The logo is the text under VorTel omit.It should not be playful but Profesionel

Font styles to use
Sans Serif

Colors
0555a3
3176b5
85abd2
85cae6
34a7d8
0792cd
cee9f5
cfdfed
000000

Requirements
Must have
• Color like business card, Please, with the text under VorTel, Correct address Rimbachstr. 4 Zip code 9517 Goldach, as well as Couvert Without addressing only design and logo with VorTal
Nice to have
• more writing articles
Should not have
• Not too colored, Text under VorTel, bright colors

```html
<!DOCTYPE html>
<html lang="en">
<head>
<meta charset="utf-8">
<title>VorTel Gmbh – Letterhead</title>
<link href="https://fonts.googleapis.com/css2?family=Lato:wght@400;700;900&display=swap" rel="stylesheet">
<style>
  :root {
    --backdrop: #404040;
    --paper: #ffffff;
    --navy: #061a6e;
    --steel: #7ea6c0;
    --ink: #000000;
  }
  * { margin: 0; padding: 0; box-sizing: border-box; }
  html, body { width: 1200px; height: 1006px; overflow: hidden; }
  body {
    background: var(--backdrop);
    font-family: "Lato", sans-serif;
    position: relative;
  }
  .letterhead {
    position: absolute;
    left: 320px; top: 78px;
    width: 577px; height: 816px;
    background: var(--paper);
    overflow: hidden;
    color: var(--ink);
  }
  .top-band {
    position: absolute; left: 0; top: 0;
    width: 100%; height: 27px;
    background: var(--navy);
  }
  .brand {
    position: absolute; left: 50px; top: 52px;
    display: flex; align-items: center; gap: 10px;
  }
  .brand-mark {
    width: 44px; height: 44px;
    background: var(--navy);
  }
  .brand-name {
    font-weight: 900; font-size: 30px;
    color: var(--navy); letter-spacing: 1px;
  }
  .salutation {
    position: absolute; left: 85px; top: 229px;
    font-size: 12px;
  }
  .letter-body {
    position: absolute; left: 85px; top: 282px;
    width: 410px;
    font-size: 11.3px; line-height: 12.5px;
    letter-spacing: -0.15px;
  }
  .letter-body p + p { margin-top: 12.5px; }
  .signature {
    position: absolute; left: 85px; top: 527px;
    width: 88px; height: 44px;
    background: linear-gradient(90deg, #eeeeee, #f7f7f7);
  }
  .signer {
    position: absolute; left: 85px; top: 590px;
    font-size: 12px; line-height: 18.5px;
  }
  .contact-line {
    position: absolute; left: 42px; top: 785px;
    display: flex; gap: 24px;
    font-size: 8.5px; color: var(--navy);
  }
  .contact-item { display: flex; align-items: center; gap: 3px; }
  .contact-item svg { width: 9px; height: 9px; }
  .divider { border-left: 1px solid var(--navy); padding-left: 4px; margin-left: 2px; }
  .footer-shapes { position: absolute; left: 0; bottom: 0; }
  .web-address {
    position: absolute; right: 26px; top: 792px;
    font-size: 11px; letter-spacing: 2.2px; color: #ffffff;
  }
</style>
</head>
<body>
  <main class="letterhead">
    <div class="top-band"></div>

    <div class="brand">
      <div class="brand-mark"></div>
      <span class="brand-name">VORTEL</span>
    </div>

    <p class="salutation">Dear Mr. Brunner,</p>

    <div class="letter-body">
      <p>Lorem ipsum dolor sit amet, consectetur adipiscing elit. Cras elementum eget sem quis tincidunt. Suspendisse congue accumsan ipsum ac auctor.</p>
      <p>Fusce sagittis tellus a urna ornare eleifend. Interdum et malesuada fames ac ante ipsum primis in faucibu. Fusce pulvinar sodales diam et consequat. Praesent placerat nulla vitae nisl ullamcorper, vel facilisis lorem consequat. Fusce sagittis tellus a urna ornare eleifend. Interdum et malesuada fames ac ante ipsum primis in faucibu. Fusce pulvinar sodales diam et consequat. Praesent placerat nulla vitae nisl ullamcorper, vel facilisis lorem consequat.</p>
      <p>Fusce sagittis tellus a urna ornare eleifend. Interdum et malesuada fames ac ante ipsum primis in faucibu. Fusce pulvinar sodales diam et consequat. Praesent placerat nulla vitae nisl ullamcorper, vel facilisis lorem consequat.</p>
      <p>Lorem ipsum dolor sit amet, consectetur adipiscing elit. Cras elementum eget sem quis tincidunt.</p>
    </div>

    <div class="signature" role="img" aria-label="Handwritten signature of Daniel Keller"></div>

    <p class="signer">Daniel Keller<br>Co Founder &amp; CEO</p>

    <div class="contact-line">
      <span class="contact-item">
        <svg viewBox="0 0 10 10"><path d="M2 1l2 2-1 1.2c.6 1.2 1.5 2.1 2.8 2.8L7 6l2 2-1.3 1.3C4.5 9 1 5.5.7 2.3z" fill="none" stroke="currentColor" stroke-width=".8"/></svg>
        +41 71 555 20 40
      </span>
      <span class="contact-item">
        <svg viewBox="0 0 10 10"><rect x=".5" y="2" width="9" height="6" fill="none" stroke="currentColor" stroke-width=".8"/><path d="M.5 2L5 5.5 9.5 2" fill="none" stroke="currentColor" stroke-width=".8"/></svg>
        info@vortel.ch
      </span>
      <span class="contact-item">
        <svg viewBox="0 0 10 10"><path d="M5 9.5S1.8 6 1.8 3.8a3.2 3.2 0 0 1 6.4 0C8.2 6 5 9.5 5 9.5z" fill="none" stroke="currentColor" stroke-width=".8"/><circle cx="5" cy="3.8" r="1.1" fill="currentColor"/></svg>
        Rimbachstr. 4 <span class="divider">9517 Goldach</span>
      </span>
    </div>

    <svg class="footer-shapes" width="577" height="40" viewBox="0 0 577 40">
      <rect x="0" y="22" width="418" height="18" fill="var(--steel)"/>
      <polygon points="434,0 577,0 577,40 414,40" fill="var(--navy)"/>
    </svg>
    <span class="web-address">www.vortel.ch</span>
  </main>
</body>
</html>
```